MALT HIGHLANDS/STONEFERN DISTILLERY

DOUBLE SIDED BUSINESS CARD ONE SIDE FOR WWW.MALTHIGHLANDS-EXAMPLE.ORG AND ONE SIDE FOR STONEFERN DISTILLERY ARTWORK FOR WEBSITE IS ATTACHED

1)
GORDON PRYCE CEO
MALT HIGHLANDS
Office 1 Harbour Court
14 Ferrier Row
Glasgow
Scotland, G5 2KX
W:WWW.MALTHIGHLANDS-EXAMPLE.ORG
E:GORDON@MALTHIGHLANDS-EXAMPLE.ORG
T:+44 7491 305718

2)
GORDON PRYCE CEO
STONEFERN DISTILLERY
Building 148, Werfpark Zandhoven,
3e Brederolaan, Katwijk, 2219KP

W: WWW.stonefern-example.nl
E: GORDON@stonefern-example.nl
T:+44 7491 305718

1)
Marieke Dool DIRECTOR
MALT HIGHLANDS
Office 1 Harbour Court
14 Ferrier Row
Glasgow
Scotland, G5 2KX
W:WWW.MALTHIGHLANDS-EXAMPLE.ORG
E:Marieke@MALTHIGHLANDS-EXAMPLE.ORG
T:+31 6 58137704

2)
MARIEKE DOOL DIRECTOR
STONEFERN DISTILLERY

E: marieke@stonefern-example.nl
T:+31 6 58137704

```html
<!DOCTYPE html>
<html lang="en">
<head>
<meta charset="utf-8">
<title>Malt Highlands / Stonefern Distillery business cards</title>
<link rel="stylesheet" href="https://fonts.googleapis.com/css2?family=Montserrat:wght@400;500;700&display=swap">
<style>
  :root {
    --page: #1c1c1d;
    --card: #2c2c2d;
    --pennant: #19191a;
    --gold: #d4a444;
    --white: #f2f2f2;
    --strip: #0e0e0e;
  }
  * { margin: 0; padding: 0; box-sizing: border-box; }
  html, body { width: 1200px; height: 800px; overflow: hidden; background: var(--page); }
  body { font-family: "Montserrat", Arial, sans-serif; }
  .stage { position: relative; width: 1200px; height: 800px; }
  .card { position: absolute; top: 175px; width: 290px; height: 450px; }
  .card--malt { left: 280px; }
  .card--stonefern { left: 630px; }
  .card-shape { position: absolute; inset: 0; width: 290px; height: 450px; }
  .brand {
    position: absolute; left: 45px; width: 201px; top: 40px;
    display: flex; flex-direction: column; align-items: center;
  }
  .brand-dot { width: 54px; height: 54px; border: 2px solid var(--gold); border-radius: 50%; margin-bottom: 26px; }
  .brand-name {
    color: var(--gold); font-weight: 700; font-size: 15px; letter-spacing: 3px;
    text-align: center; line-height: 1.5;
  }
  .person { position: absolute; left: 0; width: 290px; text-align: center; }
  .person-name { color: var(--white); font-weight: 700; font-size: 14px; letter-spacing: 2.4px; }
  .person-role, .person-company { color: var(--gold); font-size: 10px; letter-spacing: 1px; line-height: 13px; }
  .contact { position: absolute; left: 38px; display: flex; align-items: flex-start; gap: 10px; }
  .contact-icon { width: 12px; height: 12px; flex: none; margin-top: 1px; }
  .contact-text { color: var(--white); font-size: 9px; letter-spacing: 0.6px; line-height: 11px; }
  .contact-text--mail { font-size: 7.4px; letter-spacing: 1px; margin-top: 2px; }
  .contact-text--address { color: var(--gold); letter-spacing: 0.8px; }
  .website {
    position: absolute; left: 0; width: 290px; text-align: center;
    color: var(--white); font-size: 7.4px; letter-spacing: 1.8px;
  }
</style>
</head>
<body>
<main class="stage">

  <section class="card card--malt" aria-label="Malt Highlands business card">
    <svg class="card-shape" viewBox="0 0 290 450" aria-hidden="true">
      <rect x="0" y="392" width="92" height="58" fill="var(--gold)"/>
      <rect x="199" y="392" width="91" height="58" fill="var(--gold)"/>
      <rect x="92" y="436" width="107" height="14" fill="var(--strip)"/>
      <path d="M0,0 H290 V394 C270,396 276,436 250,436 H40 C14,436 20,396 0,394 Z" fill="var(--card)"/>
      <path d="M45,0 H246 V164 L143,233 L45,164 Z" fill="var(--pennant)"/>
    </svg>
    <div class="brand">
      <div class="brand-dot"></div>
      <div class="brand-name">MALT<br>HIGHLANDS</div>
    </div>
    <div class="person" style="top:239px">
      <div class="person-name">GORDON PRYCE</div>
      <div class="person-role">CEO</div>
      <div class="person-company">MALT HIGHLANDS</div>
    </div>
    <div class="contact" style="top:295px">
      <svg class="contact-icon" viewBox="0 0 24 24" aria-hidden="true"><path fill="var(--gold)" d="M6.6 10.8a15 15 0 0 0 6.6 6.6l2.2-2.2a1 1 0 0 1 1-.25 11.4 11.4 0 0 0 3.6.57 1 1 0 0 1 1 1V20a1 1 0 0 1-1 1A17 17 0 0 1 3 4a1 1 0 0 1 1-1h3.5a1 1 0 0 1 1 1c0 1.25.2 2.45.57 3.57a1 1 0 0 1-.25 1Z"/></svg>
      <span class="contact-text">+44 7491 305718</span>
    </div>
    <div class="contact" style="top:315px">
      <svg class="contact-icon" viewBox="0 0 24 24" aria-hidden="true"><path fill="var(--gold)" d="M2 5h20v14H2Z"/><path d="M2 5l10 8 10-8" fill="none" stroke="var(--card)" stroke-width="2"/></svg>
      <span class="contact-text contact-text--mail">GORDON@MALTHIGHLANDS-EXAMPLE.ORG</span>
    </div>
    <div class="contact" style="top:338px">
      <svg class="contact-icon" viewBox="0 0 24 24" aria-hidden="true"><path fill="var(--gold)" d="M12 2a7 7 0 0 0-7 7c0 5 7 13 7 13s7-8 7-13a7 7 0 0 0-7-7Zm0 9.5A2.5 2.5 0 1 1 12 6.5a2.5 2.5 0 0 1 0 5Z"/></svg>
      <span class="contact-text contact-text--address">Office 1 Harbour Court<br>14 Ferrier Row<br>Glasgow<br>Scotland, G5 2KX</span>
    </div>
    <div class="website" style="top:414px">WWW.MALTHIGHLANDS-EXAMPLE.ORG</div>
  </section>

  <section class="card card--stonefern" aria-label="Stonefern Distillery business card">
    <svg class="card-shape" viewBox="0 0 290 450" aria-hidden="true">
      <rect x="0" y="392" width="92" height="58" fill="var(--gold)"/>
      <rect x="199" y="392" width="91" height="58" fill="var(--gold)"/>
      <rect x="92" y="436" width="107" height="14" fill="var(--strip)"/>
      <path d="M0,0 H290 V394 C270,396 276,436 250,436 H40 C14,436 20,396 0,394 Z" fill="var(--card)"/>
      <path d="M45,0 H246 V169 L145,238 L45,169 Z" fill="var(--pennant)"/>
    </svg>
    <div class="brand">
      <div class="brand-dot"></div>
      <div class="brand-name">STONEFERN<br>DISTILLERY</div>
    </div>
    <div class="person" style="top:243px">
      <div class="person-name">GORDON PRYCE</div>
      <div class="person-role">CEO</div>
      <div class="person-company">STONEFERN DISTILLERY</div>
    </div>
    <div class="contact" style="top:302px">
      <svg class="contact-icon" viewBox="0 0 24 24" aria-hidden="true"><path fill="var(--gold)" d="M6.6 10.8a15 15 0 0 0 6.6 6.6l2.2-2.2a1 1 0 0 1 1-.25 11.4 11.4 0 0 0 3.6.57 1 1 0 0 1 1 1V20a1 1 0 0 1-1 1A17 17 0 0 1 3 4a1 1 0 0 1 1-1h3.5a1 1 0 0 1 1 1c0 1.25.2 2.45.57 3.57a1 1 0 0 1-.25 1Z"/></svg>
      <span class="contact-text">+44 7491 305718</span>
    </div>
    <div class="contact" style="top:322px">
      <svg class="contact-icon" viewBox="0 0 24 24" aria-hidden="true"><path fill="var(--gold)" d="M2 5h20v14H2Z"/><path d="M2 5l10 8 10-8" fill="none" stroke="var(--card)" stroke-width="2"/></svg>
      <span class="contact-text contact-text--mail">GORDON@STONEFERN-EXAMPLE.NL</span>
    </div>
    <div class="contact" style="top:345px">
      <svg class="contact-icon" viewBox="0 0 24 24" aria-hidden="true"><path fill="var(--gold)" d="M12 2a7 7 0 0 0-7 7c0 5 7 13 7 13s7-8 7-13a7 7 0 0 0-7-7Zm0 9.5A2.5 2.5 0 1 1 12 6.5a2.5 2.5 0 0 1 0 5Z"/></svg>
      <span class="contact-text contact-text--address">Building 148, Werfpark Zandhoven,<br>3e Brederolaan, Katwijk, 2219KP</span>
    </div>
    <div class="website" style="top:411px">WWW.STONEFERN-EXAMPLE.NL</div>
  </section>

</main>
</body>
</html>
```